Deliver a professional and engaging investment propsal.

I am appealing to highend smart investors and need a high quality, engaging and formal presentation in PDF.
StowBin: https://www.stowbin.net/sh/qwmtr48kelvan2x/ZZTrPHmLe7WqsnBFjQ4kR8vYt?dl=0
Text for project is in Stowbin called New Proposal Final
Along with past much older attempts of this job.
Any additional ideas to enable a better outcome would be appreicated.

```html
<!DOCTYPE html>
<html lang="en">
<head>
<meta charset="utf-8">
<title>Ridgeline Business Park – Project Proposal</title>
<link href="https://fonts.googleapis.com/css2?family=Roboto:ital,wght@0,400;0,500;0,700;1,400;1,700&display=swap" rel="stylesheet">
<style>
:root{
  --blue:#1565c0;
  --blue-dark:#0d4a94;
  --blue-light:#6fa8dc;
  --ink:#2a2a2a;
  --stage:#cdd0d4;
  --canvas:#ffffff;
  --line:#d6dbe2;
  --red:#e53935;
}
*{box-sizing:border-box;margin:0;padding:0}
html,body{width:1200px;height:2187px;overflow:hidden;background:var(--canvas);font-family:"Roboto",Arial,sans-serif;color:var(--ink)}
.sheet{position:relative;width:1200px;height:2187px}
.stage{position:absolute;left:80px;top:0;width:1040px;height:554px;background:var(--stage)}
.cover{position:absolute;left:430px;top:34px;width:340px;height:480px;background:linear-gradient(180deg,#3a6ea5 0%,#7fa4c8 40%,#c9a070 70%,#6b4d3a 100%);box-shadow:0 10px 24px rgba(0,0,0,.25);overflow:hidden}
.cover-title{position:absolute;left:24px;top:30px;right:24px;padding:14px 16px;background:rgba(255,255,255,.55);border:1.5px solid #fff}
.cover-title .kicker{font-size:22px;font-weight:700;color:#1e3552;line-height:1.05;text-transform:uppercase}
.cover-title .name{font-size:22px;font-weight:500;color:var(--blue-dark);margin-top:4px}
.cover-title .sub{font-size:11px;font-weight:700;color:#1e3552;margin-top:4px;text-transform:uppercase}
.cover-contact{position:absolute;left:24px;bottom:26px;width:200px;padding:10px 12px;background:rgba(255,255,255,.6);border:1.5px solid #fff;font-size:9px;color:#1e3552;line-height:1.5}
.cover-contact strong{display:block;font-size:10px;margin-bottom:4px}
.page{position:absolute;background:#fff;box-shadow:0 2px 10px rgba(0,0,0,.18);padding:18px 20px 30px;font-size:7px;line-height:1.36;color:var(--ink);overflow:hidden}
.p1{left:245px;top:566px;width:313px;height:503px;padding:0 0 30px}
.p2{left:630px;top:566px;width:356px;height:503px;padding-top:22px}
.p3{left:44px;top:1094px;width:354px;height:498px}
.p4{left:424px;top:1094px;width:356px;height:498px}
.p5{left:806px;top:1094px;width:356px;height:498px}
.p6{left:44px;top:1618px;width:354px;height:503px}
.p7{left:424px;top:1618px;width:356px;height:503px}
.p8{left:806px;top:1618px;width:356px;height:503px;padding:14px}
.heading{display:flex;align-items:center;gap:5px;font-size:17px;font-weight:500;color:var(--blue);margin-bottom:10px;line-height:1.1}
.heading::before{content:"";width:12px;height:12px;background:var(--blue);border-radius:2px;flex:none}
.heading.two-line{align-items:flex-start}
.heading.two-line::before{margin-top:3px}
.bullets{list-style:none}
.bullets li{position:relative;padding-left:9px;margin-bottom:8px}
.bullets li::before{content:"";position:absolute;left:1px;top:3px;width:3px;height:3px;border-radius:50%;background:var(--blue)}
p{margin-bottom:7px}
.footer{position:absolute;left:14px;right:14px;bottom:10px;height:8px;border-bottom:1.5px solid var(--blue)}
.footer .tab{position:absolute;bottom:-1.5px;height:8px;padding:0 22px;background:var(--blue);color:#fff;font-size:5.5px;font-weight:700;line-height:8px;clip-path:polygon(6% 0,100% 0,94% 100%,0 100%)}
.footer .num{position:absolute;bottom:1px;width:7px;height:7px;border:1px solid var(--blue);border-radius:50%;font-size:4.5px;color:var(--blue);text-align:center;line-height:5px}
.left .tab{left:110px}.left .num{left:0}
.right .tab{left:20px}.right .num{right:0}
.photo{background:linear-gradient(180deg,#3d5f8a 0%,#7f8fa5 50%,#8a6a50 100%)}
.hero{height:165px}
.siteplan{margin:6px 16px 0;height:152px;background:linear-gradient(135deg,#b7c2a8,#dfe3d8 50%,#a9b69a)}
.p1 .copy{padding:8px 16px 0;color:var(--blue);font-size:6.6px}
.p1 .copy p{margin-bottom:6px}
.mapbox{margin-top:12px;height:120px;background:linear-gradient(135deg,#cfa52a,#e08a3a 50%,#c9a630)}
.growth{background:var(--blue-light);border-radius:6px;padding:8px 10px;margin-bottom:10px;color:#10375f}
.growth h4{font-size:6.5px;font-weight:700;text-transform:uppercase;margin-bottom:3px}
.growth ol{padding-left:22px;font-size:6.2px}
.growth a{color:#0a2f9e;text-decoration:underline}
.warn{color:var(--red)}
table{width:100%;border-collapse:collapse;font-size:5.6px;margin:4px 0 8px}
th{background:var(--blue);color:#fff;font-weight:700;padding:2px 4px;text-align:right}
td{padding:2.2px 4px;text-align:right;border-bottom:1px solid var(--line)}
tr.sub td{background:var(--blue);color:#fff;font-weight:700;text-align:center}
.note{font-weight:700;font-style:italic;font-size:6.6px}
.team{background:var(--blue);border-radius:8px;color:#fff;padding:8px 10px;margin-bottom:10px}
.team h5{font-size:7px;font-style:italic;font-weight:700;border-bottom:1px solid rgba(255,255,255,.7);padding-bottom:3px;margin-bottom:4px}
.team p{margin-bottom:4px}
.target{position:absolute;left:14px;right:14px;bottom:30px;height:112px;background:linear-gradient(135deg,#b9bdc2,#e4e5e6 45%,#d9b640 75%,#3b3b3b)}
.citymap{width:100%;height:100%;background:linear-gradient(160deg,#f0f2ee,#d9dfe6 45%,#f2efe6)}
</style>
</head>
<body>
<div class="sheet">

  <div class="stage"></div>
  <section class="cover photo" aria-label="Proposal cover">
    <div class="cover-title">
      <div class="kicker">Project<br>Proposal</div>
      <div class="name">Ridgeline Business Park</div>
      <div class="sub">60 Acre Mixed-Use<br>Development</div>
    </div>
    <div class="cover-contact">
      <strong>Please send all questions and all joint venture proposals to:</strong>
      Daniel Marsh<br>dmarsh.invest@example.com<br>+61 400 555 019
    </div>
  </section>

  <section class="page p1">
    <div class="photo hero" role="img" aria-label="Photograph of a three-storey hotel building at dusk"></div>
    <div class="copy">
      <p>We have an incredible property, Ridgeline Business Park, located at 1180 Route 40 Larkin County, Ridgeford City, 58901 USA which we have fully funded with cash and now need a joint venture partner, buyer or lender to get this project to completion and producing a substantial profit we all can share.</p>
      <p>Our property is located on the best oil reserves in the world, with more oil than any other county in the basin and with the lowest recoverable costs of $24 a barrel.</p>
      <p>We own the property and need a partner to develop the site and bring to the market at half the cost of competing business parks in the area.</p>
    </div>
    <div class="siteplan" role="img" aria-label="Site plan of the business park showing lots, roads and buildings"></div>
    <div class="footer left"><span class="num">1</span><span class="tab">Ridgeline Business Park</span></div>
  </section>

  <section class="page p2">
    <h2 class="heading">Participation Options</h2>
    <ul class="bullets">
      <li>A joint venture partner would support all the costs developing the property without the upfront costs of the property purchase.</li>
      <li>All sales would be split to ensure both parties are paid out in such a way that both are paid out in full at the same time then a 50/50 profit share split on all remaining sales.</li>
      <li>Contract drawn up protecting and supporting both parties on agreed terms.</li>
      <li>As a potential joint venture partner, I would cover the full property (57.7 acres) cost as mentioned of $124,784 per acre (57.7 acres). ($7,200,000)</li>
      <li>Joint venture partner to supply the development costs estimated to be around $65,000 an acre estimated pending tender selection and additional refundable security bonds held with the Ridgeford City on development works.</li>
      <li>Development costs could be in up to three stages to lower outlay and limit exposure if so desired, however it will take longer to complete and bring to market.</li>
      <li>A buyer can be fully supported by myself to oversee the full project and outcomes and support the budgets of construction and sales to get the highest returns for a small fee.</li>
      <li>To purchase the property, you would need to contact me directly and I can introduce you to our realtor who will discount his commission from 6% to 5% which is a significant saving.</li>
      <li>Financing on excellent terms allowing 12 to 18 months for income streams and could be linked to a joint venture option / profit share.</li>
    </ul>
    <div class="footer right"><span class="tab">Ridgeline Business Park</span><span class="num">2</span></div>
  </section>

  <section class="page p3">
    <h2 class="heading">Major Site Changes</h2>
    <ul class="bullets">
      <li>We purchased the property in in 2013 for cash and without any additional debt, at the time we had Route 40 frontage just outside Ridgeford City limits South of town with a zoning of agricultural within Larkin County.</li>
      <li>2014 site zoning changed allowing a commercial zoning.</li>
      <li>Flag Hotel site purchased 2014 now with the option to purchase the franchise license and build the hotel ourselves.</li>
      <li>In 2016 we were added into City Limits which was a massive improvement to our site now taking advantage of confirmed city water and sewer was a great outcome.</li>
      <li>In 2016 the new bypass opened intersecting our highway frontage just 100 yards away which brings all the traffic in the basin right past our site which was a massive win for this project.</li>
      <li>Same commercial property listed across the road at $750,000 per acre retail at Ashby Commons and other business parks average listings $550,00 per acre.</li>
      <li>In late 2017 we applied for full site development application and were approved in mid-2018 which again was a significant improvement to the project.</li>
      <li>May 2018 Full site infrastructure development approval which includes all roads and city services, this will trigger interest in the site from passing traffic and with a great marketing campaign will surely start sales coming in quickly once we break ground and start work.</li>
      <li>We also can buy the franchise license of the Harbor Crest hotel for additional income potential if desired.</li>
    </ul>
    <div class="footer left"><span class="num">3</span><span class="tab">Ridgeline Business Park</span></div>
  </section>

  <section class="page p4">
    <h2 class="heading">Location</h2>
    <ul class="bullets">
      <li>Our property is ideally located in Ridgeford City, United States of America, despite its humble beginnings, has suddenly found itself at the epicentre of the oil boom. The city has seen workers flood into the area over recent years to fill positions to support the growth.</li>
      <li>Larkin County where Ridgeford City is located has more recoverable oil and gas at the lowest recoverable cost per barrel at $24, making it most affordable anywhere in the basin, centrally located and very desirable area to establish a business and company headquarters.</li>
      <li>Ridgeford City is the crossroads whereby around 20,000 vehicles pass by our site each day travelling locally and between Brennan where boom started and Halvorsen, our project has highway frontage and is 100 yards away from the bypass intersection making it the best location in Larkin County for this type of project.</li>
      <li>With billions invested into infrastructure in the past 5 years in and around the shale oil basin our project has become the beneficiary of a major new Ridgeford City bypass which intersects Route 40 just 100 yards south of our project, putting us on one of the busiest intersections in the basin.</li>
      <li>Demand stems from the ongoing boom in oil and gas drilling in the area which is still in its infancy stages of life and is expected to continue to grow well past 2050 based on obtainable reserves beneath the ground.</li>
    </ul>
    <div class="mapbox" role="img" aria-label="Regional map of counties with Ridgeford City highlighted"></div>
    <div class="footer right"><span class="tab">Ridgeline Business Park</span><span class="num">4</span></div>
  </section>

  <section class="page p5">
    <div class="growth">
      <h4>Additional location growth:</h4>
      <ol>
        <li><a>Northfield 150 million-dollar Ridgeford City investment 2018</a></li>
        <li><a>The state is the nation's second-biggest oil producer</a></li>
        <li><a>Larkin County Investment, Development</a></li>
      </ol>
    </div>
    <p>Within the 100 yards of Ridgeline Business park, directly across the road commercial land is currently listed at $750,000 an acre at Ashby Commons and many more locations up to $650,000 per acre. With an advantage over other sites in terms of a better location and much lower purchase and development costs the numbers don't lie, and we need to have pad ready to build lots to offer the market.</p>
    <p>Basin traffic, North, South, East and West will have to travel right by our site making it the second busiest intersection in the area, giving us the best exposure to sell, promote and grow, this site can and will be the location for new business and growth, we need to develop the site now to move forward.</p>
    <p>With our obvious high exposure to potential buyers through the passing traffic and lower entry price point there is no doubt Ridgeline Town Center will become the place where business will want to build alongside a quality business like the Harbor Crest Suites Hotel.</p>
    <h2 class="heading" style="margin-top:14px">Harbor Crest Suites</h2>
    <p>Harbor Crest Hotels' unmatched experience and leadership in the hotel industry designed a new extended stay hotel that satisfy one of the most in-demand needs of today's business and leisure travellers.</p>
    <p>Here guests will experience the very best in hotel and home. Its flexible spaces, stylish design, and brand signature elements come together to create an enriching extended stay experience for your guests, while building loyalty and repeat bookings for your hotel.</p>
    <div class="footer left"><span class="num">5</span><span class="tab">Ridgeline Business Park</span></div>
  </section>

  <section class="page p6">
    <h2 class="heading">Sensitivity Analysis</h2>
    <p>Sensitivity analysis is based on sales of the full site. (45 saleable acres) Our numbers below don't include revenue from build to suit projects or potential income stream from construction of the motel and various projects that could be developed on this 60-acre site.</p>
    <p class="warn">These costs are only shown as estimates at this stage.</p>
    <table>
      <tr><th>Estimated Projections</th><th>Projected</th><th>Best Scenario</th><th>Worst Scenario</th></tr>
      <tr><td>Average sale per acre (45)</td><td>$450,000</td><td>$500,000</td><td>$350,000</td></tr>
      <tr><td>Total Sales</td><td>$20,250,000</td><td>$22,500,000</td><td>$15,750,000</td></tr>
      <tr class="sub"><td colspan="4">Projected Expenses</td></tr>
      <tr><td>Engineers</td><td>$250,000</td><td>$190,000</td><td>$300,000</td></tr>
      <tr><td>Estimated Site Development Works</td><td>$2,500,000</td><td>$2,000,000</td><td>$3,500,000</td></tr>
      <tr><td>Site Licences / Permits</td><td>$450,000</td><td>$350,000</td><td>$500,000</td></tr>
      <tr><td>Additional Signage, Marketing</td><td>$20,000</td><td>$15,000</td><td>$25,000</td></tr>
      <tr><td>Professional Fees</td><td>$135,000</td><td>$130,000</td><td>$145,000</td></tr>
      <tr><td>Attorney Contracts / Support</td><td>$45,000</td><td>$30,000</td><td>$50,000</td></tr>
      <tr><td>Realtor Commissions</td><td>$1,000,000</td><td>$900,000</td><td>$1,200,000</td></tr>
      <tr><td>Property Payout</td><td>$7,200,000</td><td>$7,200,000</td><td>$7,200,000</td></tr>
      <tr><td>Estimated Projected Full Costs</td><td>$11,580,000</td><td>$10,815,000</td><td>$12,920,000</td></tr>
      <tr><td>Estimated Projected Per Acre Costs</td><td>$253,000</td><td>$240,000</td><td>$287,000</td></tr>
      <tr><td>Estimated Total Projected Profit</td><td>$8,750,000</td><td>$11,685,000</td><td>$2,830,000</td></tr>
      <tr><td>Estimated Profit Each Partner</td><td>$4,375,000</td><td>$5,842,500</td><td>$1,415,000</td></tr>
    </table>
    <p class="note">This investment may offer an opportunity for a visa into the USA however you will need to undertake your own inquires.</p>
    <div class="footer right"><span class="tab">Ridgeline Business Park</span><span class="num">6</span></div>
  </section>

  <section class="page p7">
    <h2 class="heading">About Our Quality Team</h2>
    <div class="team">
      <h5>Owner - Daniel Marsh</h5>
      <p>I am an investor always seeking great value opportunities.</p>
    </div>
    <div class="team">
      <h5>Our Kestrel Engineering Design and Planning</h5>
      <p>From planning to conceptual design to construction services, our planning department understands the innovative solutions needed for your project needs. Our planners collaborate with other design professions to create innovative solutions for planning projects and other design needs. Kestrel designs with nature in mind and creating sustainable solutions to each unique and individual design requirement. Our pursuit is to bring the public solid goals and concepts by challenging old convention and implementing new life-giving communities and spaces.</p>
      <p>We have experience and capabilities in conceptual project development, master planning, feasibility studies, park and recreational design, urban and land planning.</p>
    </div>
    <h2 class="heading">In Conclusion</h2>
    <p>This is a solid project located in the basin on top of the most cost-effective oil reserves anywhere in the region, centrally located for business and with highway frontage and now with the new Bypass intersection at our doorstep, it creates an incredible opportunity.</p>
    <p>I would love to have you come on board as partner, our focus is pushing hard and fast to take advantage of the window of opportunity with the weather in March next year and have everything ready to roll and have lots ready for sale before August 2019.</p>
    <div class="target photo" role="img" aria-label="Photograph of a hand placing a dart on a target"></div>
    <div class="footer left"><span class="num">7</span><span class="tab">Ridgeline Business Park</span></div>
  </section>

  <section class="page p8">
    <div class="citymap" role="img" aria-label="Ridgeford City development map with legend, titled Ridgeford City is re-investing in itself"></div>
  </section>

</div>
</body>
</html>
```